Corvella Foundation is a new grant making charity set up in the UK.

Having got a logo, we now need a website to go with it. We have worked out the text which people are going to need in order to then apply for grants. But having found out what we require they will probably need to go away and think about it.
We have to be careful of what images we use. So I have uploaded some images that we like. We are also going to be adding more pages almost immediately so need to think about the images for these.
I know basic wordpress so I will be able to add new pages/make alterations in future.
Updates
The website does need to be coded in Wordpress so that I can maintain it afterwards.
Marisse
Brief changed to provide more money and we have also provided more possible pictures. And generally more explanation.
Target Market(s)
departments in universities, other charities doing work on relief of pain, people working in health service departments
Industry/Entity Type
Health Charity
Coding
Coded - Design and coding required
Number of Pages Required
4 page
Look and feel
Each slider illustrates characteristics of the customer's brand and the style your logo design should communicate.

```html
<!DOCTYPE html>
<html lang="en">
<head>
<meta charset="utf-8">
<title>Corvella Foundation</title>
<link href="https://fonts.googleapis.com/css2?family=Montserrat:wght@400;500;600;700&display=swap" rel="stylesheet">
<style>
:root{
  --blue:#0b6fbf;
  --blue-dark:#075a9c;
  --ink:#333;
  --muted:#555;
  --light:#f5f5f5;
  --white:#fff;
  --footer:#141414;
  --footer-bar:#0a0a0a;
}
*{box-sizing:border-box;margin:0;padding:0}
html,body{width:1200px;height:3638px;overflow:hidden}
body{position:relative;font-family:'Montserrat',sans-serif;color:var(--ink);background:var(--white)}
.abs{position:absolute}
.topbar{left:0;top:0;width:1200px;height:42px;background:#f1f1f4;font-size:13px;text-align:right;padding:8px 124px 0 0;letter-spacing:.5px}
.topbar b{font-weight:700}
.header{left:0;top:42px;width:1200px;height:70px;background:var(--white)}
.brand{display:flex;align-items:center;gap:12px}
.brand-mark{width:34px;height:34px;background:var(--blue);flex:none}
.brand-name{font-size:26px;font-weight:700;color:var(--blue);letter-spacing:.5px;line-height:1.1;white-space:nowrap}
.header .brand{position:absolute;left:123px;top:15px}
.header .brand-name{font-size:18px}
.nav{position:absolute;top:28px;font-size:13px;letter-spacing:.5px;color:#444}
.nav.active{color:var(--blue)}
.btn{background:var(--blue);color:var(--white);font-weight:600;letter-spacing:1px;display:flex;align-items:center;justify-content:center}
.hero{left:0;top:112px;width:1200px;height:577px;background:radial-gradient(ellipse at 65% 40%,#2a63b8 0%,#123a78 35%,#08152f 75%,#050c1c 100%)}
.hero-title{left:124px;top:292px;font-size:34px;font-weight:700;color:var(--white);letter-spacing:1px}
.hero-sub{left:124px;top:338px;font-size:18px;font-weight:600;color:var(--white)}
.hero-aim{left:124px;top:370px;font-size:16px;color:var(--white);line-height:23px;letter-spacing:.6px}
.hero-aim b{font-weight:700}
.section-title{width:1200px;left:0;text-align:center;font-size:35px;font-weight:700;color:#333;letter-spacing:1px}
.card{background:var(--white);box-shadow:0 2px 10px rgba(0,0,0,.09);text-align:center;padding:0 24px}
.card h3{font-size:14.5px;font-weight:500;line-height:22px;color:#222;margin-top:56px}
.card p{font-size:12px;line-height:18px;color:var(--muted);margin-top:10px}
.icon-circ{width:79px;height:79px;border-radius:50%;background:var(--blue);display:flex;align-items:center;justify-content:center}
.aim{left:0;top:1536px;width:600px;height:508px;background:var(--blue)}
.aim-art{left:600px;top:1536px;width:600px;height:508px;background:radial-gradient(ellipse at 55% 45%,#e8702a 0%,#a33a14 30%,#3a1a12 60%,#141414 100%)}
.aim-title{left:163px;top:1740px;font-size:40px;font-weight:700;color:var(--white);line-height:46px;letter-spacing:1.5px}
.aim-sub{left:161px;top:1893px;font-size:16px;font-weight:600;color:var(--white);line-height:25px;letter-spacing:1.5px}
.grants{left:0;top:2044px;width:1200px;height:826px;background:var(--light)}
.rule{width:56px;height:3px;background:var(--blue)}
.gtext{left:150px;width:900px;text-align:center;font-size:13px;line-height:22px;color:#444}
.gitem{font-size:15px;font-weight:600;color:#222;line-height:18px}
.gicon{width:79px;height:79px;border-radius:50%;background:var(--white);box-shadow:0 2px 8px rgba(0,0,0,.1);display:flex;align-items:center;justify-content:center}
.gicon.on{background:var(--blue)}
.hub{left:455px;top:2392px;width:290px;height:290px;border-radius:50%;background:var(--white);display:flex;align-items:center;justify-content:center}
.contact-dark{left:0;top:3225px;width:1200px;height:368px;background:var(--footer)}
.contact-box{left:247px;top:2941px;width:706px;height:395px;background:var(--blue);border:5px solid var(--white);box-shadow:0 0 0 1px #ddd}
.contact-title{left:247px;width:706px;top:2980px;text-align:center;font-size:35px;font-weight:700;color:var(--white);letter-spacing:1px}
.field{background:var(--white);font-size:12px;color:#666;padding:13px 12px}
.submit{left:543px;top:3243px;width:113px;height:44px;border:2px solid var(--white);color:var(--white);font-size:14px;font-weight:600;display:flex;align-items:center;justify-content:center;letter-spacing:.5px}
.footer .brand-name{font-size:24px}
.social{width:34px;height:34px;border:1px solid #ddd}
.divider{width:1px;height:168px;background:#333;top:3400px}
.fhead{font-size:14px;font-weight:600;color:var(--white);letter-spacing:1px}
.fhead::after{content:"";display:block;width:34px;height:2px;background:#888;margin-top:10px}
.flink{font-size:13px;color:#ddd}
.flink.active{color:var(--blue)}
.fdetail{font-size:13px;color:#eee;line-height:19px;display:flex;gap:10px;align-items:flex-start}
.copy{left:0;top:3593px;width:1200px;height:45px;background:var(--footer-bar);color:#ddd;font-size:13px;text-align:center;line-height:45px}
</style>
</head>
<body>

<div class="abs topbar">Charity registration number <b>1187640.</b></div>

<header class="abs header">
  <div class="brand"><span class="brand-mark" style="width:36px;height:36px"></span><span class="brand-name">CORVELLA<br>FOUNDATION</span></div>
  <span class="nav active" style="left:498px">HOME</span>
  <span class="nav" style="left:589px">ABOUT</span>
  <span class="nav" style="left:685px">GRANTS</span>
  <span class="nav" style="left:789px">CONTACT</span>
  <div class="btn" style="position:absolute;left:904px;top:17px;width:172px;height:37px;font-size:13px">APPLY FOR GRANTS</div>
</header>

<section class="abs hero" role="img" aria-label="Glowing blue network of nerve cells on a dark background"></section>
<h1 class="abs hero-title">CORVELLA FOUNDATION</h1>
<p class="abs hero-sub">is a grant making charity set up in the UK in 2021</p>
<p class="abs hero-aim">THE MAIN AIM OF CORVELLA FOUNDATION IS<br><b>TO REDUCE THE SUFFERING CAUSED BY<br>CHRONIC PAIN.</b></p>
<div class="abs btn" style="left:124px;top:462px;width:206px;height:43px;font-size:15px">APPLY FOR GRANTS</div>

<h2 class="abs section-title" style="top:758px">ABOUT US</h2>

<div class="abs card" style="left:161px;top:887px;width:277px;height:264px">
  <h3>Who are the trustees of<br>Corvella Foundation?</h3>
  <p>The initial trustees are Marisse, Julian &amp; Ellis Delacourt. A fourth trustee is about to be appointed, the legal firm of Harlow Penrose.</p>
</div>
<div class="abs card" style="left:462px;top:887px;width:276px;height:264px">
  <h3>Who are the medical advisers<br>to Corvella Foundation?</h3>
  <p>The medical advisers are doctors or other health professionals, who individually or collectively advise the trustees on the merit of grant applications. Medical advisers are initially appointed for a five year term.</p>
</div>
<div class="abs card" style="left:761px;top:887px;width:278px;height:264px">
  <h3>How much money does<br>Corvella Foundation have?</h3>
  <p>It is unclear how much money the Foundation will have in a few years time, but currently it has about a million pounds.</p>
</div>
<div class="abs card" style="left:161px;top:1213px;width:428px;height:245px">
  <h3>Where has this money come from?</h3>
  <p>The million pounds has been inherited from Marisse's father, the late Sir Edmund Ashcombe, who had a large stake in the Ashcombe supermarket business. Further significant money is going to come from the sale of the farm where the Delacourt family currently live.</p>
</div>
<div class="abs card" style="left:611px;top:1213px;width:428px;height:245px">
  <h3>Why is the foundation named after<br>Marisse Delacourt?</h3>
  <p>Marisse Delacourt suffered from extreme pain for many years after a successful operation to cure her cancer of the tongue. Although the pain is now well controlled, the family would like the unexpected receipt of such a large amount of money from the farm, to help prevent other people going through such a difficult time.</p>
</div>

<div class="abs icon-circ" style="left:260px;top:848px"><svg width="44" height="44" viewBox="0 0 44 44" fill="none" stroke="#fff" stroke-width="2"><circle cx="12" cy="10" r="4"/><circle cx="32" cy="10" r="4"/><circle cx="22" cy="14" r="4"/><path d="M4 30v-8a6 6 0 0 1 12 0M28 22a6 6 0 0 1 12 0v8M14 36v-8a8 8 0 0 1 16 0v8"/></svg></div>
<div class="abs icon-circ" style="left:560px;top:848px"><svg width="44" height="44" viewBox="0 0 44 44" fill="none" stroke="#fff" stroke-width="2"><rect x="6" y="20" width="32" height="18" rx="2"/><circle cx="22" cy="10" r="6"/><path d="M14 38v-8a8 8 0 0 1 16 0v8M18 42h8"/></svg></div>
<div class="abs icon-circ" style="left:861px;top:848px"><svg width="44" height="44" viewBox="0 0 44 44" fill="none" stroke="#fff" stroke-width="2"><path d="M16 6h12l-4 8h-4zM20 14C8 20 8 40 22 40s14-20 2-26"/><circle cx="22" cy="28" r="7"/><path d="M22 23v10"/></svg></div>
<div class="abs icon-circ" style="left:335px;top:1174px"><svg width="44" height="44" viewBox="0 0 44 44" fill="none" stroke="#fff" stroke-width="2"><circle cx="22" cy="22" r="9"/><path d="M22 17v10M22 4v6M22 34v6M4 22h6M34 22h6M9 9l4 4M31 31l4 4M9 35l4-4M31 13l4-4"/></svg></div>
<div class="abs icon-circ" style="left:785px;top:1174px"><svg width="44" height="44" viewBox="0 0 44 44" fill="none" stroke="#fff" stroke-width="2"><circle cx="20" cy="22" r="14"/><path d="M16 32l18-18 4 4-18 18-6 2z"/></svg></div>

<section class="abs aim"></section>
<svg class="abs" style="left:161px;top:1645px" width="82" height="82" viewBox="0 0 82 82" fill="none" stroke="#fff" stroke-width="2.5"><circle cx="38" cy="44" r="34"/><circle cx="38" cy="44" r="24"/><circle cx="38" cy="44" r="13"/><circle cx="38" cy="44" r="3" fill="#fff"/><path d="M38 44L72 10M64 4l2 10 10 2"/></svg>
<h2 class="abs aim-title">THE MAIN AIM<br>OF CORVELLA<br>FOUNDATION</h2>
<p class="abs aim-sub">IS TO REDUCE THE SUFFERING<br>CAUSED BY CHRONIC PAIN.</p>
<div class="abs aim-art" role="img" aria-label="Illustration of a seated human figure with glowing skeleton showing pain"></div>

<section class="abs grants"></section>
<h2 class="abs section-title" style="top:2114px">GRANTS</h2>
<div class="abs rule" style="left:572px;top:2160px"></div>
<p class="abs gtext" style="top:2184px">Grants will almost entirely be provided for research or education into pain management, or the prevention of pain.</p>
<p class="abs gtext" style="top:2216px">The trustees will also be providing grants to a number of other charities or to areas with which they have had a long term association, such as HIV/AIDS and TB. There is no application procedure for these other areas, and unsolicited applications are unlikely to be favorably considered by the trustees</p>
<p class="abs gtext" style="top:2304px;font-weight:600;color:#111">The main categories of funding for pain research or education will be as follows.</p>

<div class="abs hub"><div class="brand"><span class="brand-mark" style="width:30px;height:30px"></span><span class="brand-name" style="font-size:22px">CORVELLA<br>FOUNDATION</span></div></div>

<div class="abs gicon on" style="left:358px;top:2383px"><svg width="40" height="40" viewBox="0 0 40 40" fill="none" stroke="#fff" stroke-width="2"><rect x="12" y="10" width="14" height="26"/><rect x="4" y="20" width="8" height="16"/><path d="M16 16h6M16 22h6M16 28h6M19 2v6M16 5h6M30 36V26M26 30a4 4 0 0 1 8 0"/></svg></div>
<span class="abs gitem" style="left:243px;top:2414px">Pain Centres</span>

<div class="abs gicon" style="left:330px;top:2497px"><svg width="40" height="40" viewBox="0 0 40 40" fill="none" stroke="#333" stroke-width="1.6"><path d="M20 4v34M4 10c6 0 10 4 16 4s10-4 16-4M8 14c4 0 8 4 12 4s8-4 12-4"/><path d="M15 22c5-3 10 3 5 6s-5 6 0 6"/></svg></div>
<span class="abs gitem" style="left:146px;top:2520px;width:166px;text-align:right">Improving The Use<br>of Medication</span>

<div class="abs gicon" style="left:358px;top:2613px"><svg width="40" height="40" viewBox="0 0 40 40" fill="none" stroke="#333" stroke-width="1.6"><rect x="6" y="8" width="28" height="20"/><path d="M16 34h8M20 28v6M12 16l8-4 8 4-8 4zM16 18v4c2 2 6 2 8 0v-4"/></svg></div>
<span class="abs gitem" style="left:264px;top:2643px">Education</span>

<div class="abs gicon" style="left:761px;top:2383px"><svg width="40" height="40" viewBox="0 0 40 40" fill="none" stroke="#333" stroke-width="1.6"><circle cx="10" cy="22" r="7"/><path d="M10 15v14"/><rect x="16" y="14" width="22" height="10" rx="5" transform="rotate(-40 27 19)"/><circle cx="26" cy="8" r="4"/></svg></div>
<span class="abs gitem" style="left:858px;top:2414px">The Use of Opioids</span>

<div class="abs gicon" style="left:791px;top:2497px"><svg width="40" height="40" viewBox="0 0 40 40" fill="none" stroke="#333" stroke-width="1.6"><path d="M14 38v-8c-6-4-6-16 4-18s14 6 10 12l-2 2v4h-4v8"/><path d="M6 8l4 4M20 2v6M32 6l-4 4M14 4l2 4"/></svg></div>
<span class="abs gitem" style="left:887px;top:2520px">Improved Types<br>of Pain Control</span>

<div class="abs gicon" style="left:761px;top:2613px"><svg width="40" height="40" viewBox="0 0 40 40" fill="none" stroke="#333" stroke-width="1.6"><rect x="6" y="4" width="28" height="32"/><path d="M14 10v20M26 10v20M14 20h12M10 10v20M30 10v20"/></svg></div>
<span class="abs gitem" style="left:858px;top:2643px">Measuring Pain</span>

<p class="abs gtext" style="top:2746px">The trustees will initially consider unsolicited applications, <b style="font-weight:600;color:#111">for up to £50,000 each</b>, in these areas or related areas.<br>Applications for more substantial project funding will be invited in due course.</p>

<section class="abs contact-dark"></section>
<div class="abs contact-box"></div>
<h2 class="abs contact-title">CONTACT US</h2>
<div class="abs field" style="left:281px;top:3064px;width:310px;height:36px">First Name</div>
<div class="abs field" style="left:607px;top:3064px;width:312px;height:36px">Last Name</div>
<div class="abs field" style="left:281px;top:3112px;width:310px;height:36px">Email</div>
<div class="abs field" style="left:607px;top:3112px;width:312px;height:36px">Phone</div>
<div class="abs field" style="left:281px;top:3160px;width:638px;height:66px">Message</div>
<div class="abs submit">SUBMIT</div>

<footer class="footer">
  <div class="abs brand" style="left:161px;top:3404px"><span class="brand-mark" style="width:30px;height:30px"></span><span class="brand-name">CORVELLA</span></div>
  <div class="abs social" style="left:225px;top:3481px"></div>
  <div class="abs social" style="left:270px;top:3481px"></div>
  <div class="abs social" style="left:316px;top:3481px"></div>
  <div class="abs divider" style="left:487px"></div>
  <div class="abs divider" style="left:738px"></div>
  <div class="abs fhead" style="left:560px;top:3403px">QUICK LINKS</div>
  <span class="abs flink active" style="left:560px;top:3446px">Home</span>
  <span class="abs flink" style="left:560px;top:3475px">About</span>
  <span class="abs flink" style="left:560px;top:3503px">Grants</span>
  <span class="abs flink" style="left:560px;top:3532px">Contact</span>
  <div class="abs fhead" style="left:810px;top:3403px">CONTACT DETAILS</div>
  <div class="abs fdetail" style="left:810px;top:3445px"><svg width="14" height="18" viewBox="0 0 14 18"><path d="M7 0a7 7 0 0 0-7 7c0 5 7 11 7 11s7-6 7-11a7 7 0 0 0-7-7z" fill="#0b6fbf"/><circle cx="7" cy="7" r="2.5" fill="#141414"/></svg><span>14 Linden Row, Ashford Vale,<br>Kent. UK.</span></div>
  <div class="abs fdetail" style="left:810px;top:3498px;font-size:15px"><svg width="14" height="14" viewBox="0 0 14 14"><path d="M3 0l3 3-2 2c1 2 3 4 5 5l2-2 3 3-2 3C6 14 0 8 0 3z" fill="#0b6fbf"/></svg><span>020 7946 0381</span></div>
  <div class="abs fdetail" style="left:810px;top:3533px"><svg width="14" height="11" viewBox="0 0 14 11"><rect width="14" height="11" fill="#0b6fbf"/><path d="M0 0l7 6 7-6" stroke="#141414" fill="none"/></svg><span>hello@corvellafoundation.org</span></div>
</footer>
<div class="abs copy">Copyright 2021 Corvella Foundation. All Rights Reserved.</div>

</body>
</html>
```